Web Design Project

We need a web design for a legal firm based in Sydney, Australia. Our main clients are small businesses, accountants and entrepreneurs. We help our clients deal with commercial disputes and litigation.
In terms of the site design, we would like the site to appear professional, clean and easy to navigate however we would like it to be slightly more creative than the average legal website.
Legal Sites we like:
http://www.kvr.com.au/
http://www.pennystacker.com/
http://www.tiru.com/
Non-Legal Sites we like:
http://www.plevna.com/index-b.html
http://www.brimworth.com/
http://www.quillory.com/
Sites we don't like:
http://www.oregonlevyfixers.com/
We have listed below some possible colour palettes for the site:
http://www.huefanciers.com/palette/74162/Legal_Man
http://www.huefanciers.com/palette/651375/Legal_Transplant
http://www.huefanciers.com/palette/199581/Legal_Notice
Site design elements we like:
Large Footer (with newsletter sign up form)
Full screen (postwren.com, brimworth.com)
Customised Social Media icons that fit in with the style of our website
Slider
We need the following templates created:
Home Page
General Content Page
Blog
Target Market(s)
Small to Medium Sized Businesses and Entrepreneurs
Industry/Entity Type
Legal
Look and feel

```html
<!DOCTYPE html>
<html lang="en">
<head>
<meta charset="utf-8">
<title>Corvane — Legal Firm Business Services</title>
<link rel="stylesheet" href="https://fonts.googleapis.com/css2?family=Signika:wght@300;400&family=Source+Sans+3:wght@400;600&display=swap">
<style>
:root{
  --teal:#1fa9cc;
  --teal-light:#62d2e6;
  --link:#1b97c0;
  --text:#5a5a5a;
  --heading:#3a3a3a;
  --nav-top:#f8f8f0;
  --nav-bottom:#e3e4d4;
  --line:#dcdcd4;
  --footer:#ebebe7;
  --field:#e2e2d6;
  --photo-navy:#2a3f63;
  --photo-grey:#b9b9b2;
}
*{box-sizing:border-box;margin:0;padding:0}
html,body{width:840px;height:1200px;overflow:hidden}
body{background:#fff;font-family:"Source Sans 3",sans-serif;color:var(--text)}
.page{position:relative;width:840px;height:1200px;overflow:hidden}
.abs{position:absolute}
a{color:inherit;text-decoration:none}
.h{font-family:"Signika",sans-serif;font-weight:300;color:var(--heading)}

/* header */
.top-links{left:690px;top:12px;font-size:9.5px;color:#8a7a6a}
.top-links span{margin:0 6px;color:#999}
.logo{left:42px;top:36px;font-family:"Signika",sans-serif;font-weight:300;font-size:30px;color:#222;line-height:1}
.tagline{left:43px;top:69px;font-size:9px;color:#555}
.search{left:636px;top:61px;width:175px;height:20px;background:#f2f2ec;border:1px solid #dcdccd;border-radius:2px;font-size:9.5px;font-style:italic;color:#666;padding:3px 8px}
.search svg{position:absolute;right:6px;top:4px}

/* nav */
.nav{left:0;top:106px;width:840px;height:40px;background:linear-gradient(var(--nav-top),var(--nav-bottom));border-top:1px solid #d8d8c8;border-bottom:1px solid #cfd0bf}
.nav a{position:absolute;top:13px;font-size:10.5px;color:#444;letter-spacing:.2px}
.nav i{position:absolute;top:0;width:1px;height:39px;background:#d3d3c3}

/* hero */
.hero{left:0;top:146px;width:840px;height:291px;background:linear-gradient(90deg,var(--teal-light) 0%,#3fbedb 45%,var(--teal) 100%)}
.hero-photo{left:370px;top:146px;width:470px;height:291px;background:linear-gradient(90deg,rgba(63,190,219,0) 0%,#6d8ca8 35%,var(--photo-navy) 70%,#4c6a8e 100%)}
.hero-title{left:48px;top:185px;font-family:"Signika",sans-serif;font-size:19.5px;line-height:25px;color:#0f4a62}
.hero-copy{left:48px;top:241px;width:340px;font-size:8.9px;line-height:14.8px;color:#0f4d66}
.btn-more{left:47px;top:326px;width:92px;height:24px;border:1px solid #8fe3f0;border-radius:3px;background:linear-gradient(#4fc9e2,#2eb3d3);color:#fff;font-family:"Signika",sans-serif;font-size:11px;padding:4px 0 0 13px}
.dots{left:47px;top:381px}
.dots span{display:inline-block;width:15px;height:15px;background:#fff;color:#000;font-size:8.5px;text-align:center;line-height:15px;margin-right:8px}

/* main panel */
.panel{left:20px;top:412px;width:799px;height:540px;background:#fff;border-radius:3px;box-shadow:0 0 3px rgba(0,0,0,.15)}
.welcome-h{left:41px;top:428px;font-size:15.5px}
.welcome-img{left:42px;top:463px;width:95px;height:115px;background:linear-gradient(135deg,#c9b89a,#6a6e78 60%,#2b2f3a)}
.welcome-copy{font-size:8.9px;line-height:14.8px;color:var(--text)}
.read{font-size:9.5px;color:var(--link);font-weight:600;letter-spacing:.2px}
.rule{height:1px;background:var(--line)}
.blog-h{left:591px;top:427px;font-size:15.5px}
.blog-item{left:592px;width:210px}
.blog-item svg{position:absolute;left:0;top:2px}
.blog-item .t{margin-left:23px;font-size:8.9px;color:var(--link);line-height:14.8px}
.blog-item .d{margin-left:23px;font-size:8.9px;line-height:14.8px}

/* services */
.services-h{left:42px;top:689px;font-size:15.5px}
.card-img{top:716px;width:241px;height:96px;border:3px solid #fff;box-shadow:0 0 2px rgba(0,0,0,.3)}
.card-text{top:824px;width:232px}
.card-text .t{font-size:9.5px;color:var(--link);line-height:14.8px}
.card-text .d{font-size:8.9px;line-height:14.8px}

/* footer */
.footer{left:0;top:951px;width:840px;height:249px;background:var(--footer)}
.f-h{top:975px;font-size:13px}
.f-list{top:1007px;font-size:9px;line-height:20.5px;color:#555;list-style:none}
.f-list li::before{content:"›";margin-right:5px;color:#888}
.f-sep{top:976px;width:1px;height:135px;background:#dadad4}
.social{left:425px;top:1004px;font-size:9px;color:#555}
.social div{height:24.6px;position:relative;padding:2px 0 0 28px}
.social i{position:absolute;left:0;top:0;width:18px;height:18px;border-radius:50%;background:#fff;border:1px solid #d0d0c8}
.news{left:569px;top:972px;width:213px;height:139px;background:#f3f3ef;box-shadow:0 0 2px rgba(0,0,0,.08)}
.news-h{left:585px;top:983px;font-size:12.5px}
.field{left:585px;width:179px;height:21px;background:var(--field);border-radius:3px;font-size:8.5px;font-style:italic;color:#555;padding:5px 10px}
.subscribe{left:590px;top:1075px;width:76px;height:20px;background:var(--teal);border-radius:2px;color:#fff;font-size:9.5px;font-weight:600;padding:3px 0 0 13px}
.copy-rule{left:0;top:1158px;width:840px;height:1px;background:#d6d6ce}
.copyright{left:20px;top:1168px;font-size:9px;color:#666}
</style>
</head>
<body>
<div class="page">

  <div class="abs top-links">login<span>|</span>Sign up<span>|</span>FAQ's</div>
  <div class="abs logo">Corvane</div>
  <div class="abs tagline">your punch line</div>
  <div class="abs search">search here..
    <svg width="11" height="11" viewBox="0 0 11 11"><circle cx="4.5" cy="4.5" r="3.3" fill="none" stroke="#444" stroke-width="1.4"/><line x1="7" y1="7" x2="10" y2="10" stroke="#444" stroke-width="1.6"/></svg>
  </div>

  <nav class="abs nav">
    <a style="left:46px">MAIN</a><i style="left:94px"></i>
    <a style="left:119px">ABOUT US</a><i style="left:191px"></i>
    <a style="left:215px">SERVICES</a><i style="left:280px"></i>
    <a style="left:305px">TESTIMONIALS</a><i style="left:397px"></i>
    <a style="left:423px">WHY WE ARE</a><i style="left:509px"></i>
    <a style="left:531px">RECENT BLOG</a><i style="left:621px"></i>
    <a style="left:644px">NEWS</a><i style="left:696px"></i>
    <a style="left:719px">CONTACT</a>
  </nav>

  <section class="abs hero"></section>
  <div class="abs hero-photo" role="img" aria-label="Business team in suits signing documents at a meeting"></div>
  <h1 class="abs hero-title" style="font-weight:400">Legal Firm Business Services<br>goes here...</h1>
  <p class="abs hero-copy">Brightline eSolutions provides you the Search Engine Optimization making your website search engine friendly.<br>So that the website can achieve top position and ranking in the Internet searches and thereby increasing the scope for the website to be found by customers. We here modify the site to improve the ranking.</p>
  <a class="abs btn-more">learn more ›</a>
  <div class="abs dots"><span>1</span><span>2</span><span>3</span></div>

  <main class="abs panel"></main>
  <h2 class="abs h welcome-h">Welcome to Our Website Mainpage</h2>
  <div class="abs welcome-img" role="img" aria-label="Professional at a desk reviewing papers"></div>
  <p class="abs welcome-copy" style="left:150px;top:461px;width:415px">Brightline eSolutions is a web service company, offering a wide range of services which range from designing and development, that is covering almost all the fields in the best possible way. To be the best we know what and how to present beautifully the working of the client's need and their advantages to be highlighted. We act in accordance with the Industry certified processes to deliver the best to our clients all over the world.</p>
  <p class="abs welcome-copy" style="left:150px;top:549px;width:415px">Thus, Wanna get ahead in the competition with other websites…. Brightline esolutions provide you with an attractive and most convincing website to enhance your marketing goals.</p>
  <p class="abs welcome-copy" style="left:42px;top:586px;width:525px">So that the website can achieve top position and ranking in the Internet searches and thereby increasing the scope for the website to be found by customers.<br>We here modify the site to improve the ranking by using the keywords and contents.</p>
  <a class="abs read" style="left:42px;top:643px">READ MORE ›</a>
  <div class="abs rule" style="left:42px;top:660px;width:528px"></div>

  <h2 class="abs h blog-h">Recent Blog &amp; News</h2>
  <div class="abs blog-item" style="top:461px">
    <svg width="16" height="15" viewBox="0 0 16 15"><rect x="1" y="2" width="11" height="12" fill="none" stroke="#666" stroke-width="1.3"/><path d="M6 9 L14 1 L15.5 2.5 L7.5 10.5 L5.5 11 Z" fill="#666"/></svg>
    <div class="t">Backup for Enterprises: Major Benefits</div>
    <div class="d">Cloud backup solutions are becoming more and more common these days, with plans ...</div>
  </div>
  <div class="abs rule" style="left:592px;top:512px;width:208px"></div>
  <div class="abs blog-item" style="top:522px">
    <svg width="16" height="15" viewBox="0 0 16 15"><rect x="1" y="2" width="11" height="12" fill="none" stroke="#666" stroke-width="1.3"/><path d="M6 9 L14 1 L15.5 2.5 L7.5 10.5 L5.5 11 Z" fill="#666"/></svg>
    <div class="t">Backup for Enterprises: Major Benefits</div>
    <div class="d">Cloud backup solutions are becoming more and more common these days, with plans ...</div>
  </div>
  <div class="abs rule" style="left:592px;top:573px;width:208px"></div>
  <div class="abs blog-item" style="top:583px">
    <svg width="16" height="15" viewBox="0 0 16 15"><rect x="1" y="2" width="11" height="12" fill="none" stroke="#666" stroke-width="1.3"/><path d="M6 9 L14 1 L15.5 2.5 L7.5 10.5 L5.5 11 Z" fill="#666"/></svg>
    <div class="t">Backup for Enterprises: Major Benefits</div>
    <div class="d">Cloud backup solutions are becoming more and more common these days, with plans ...</div>
  </div>
  <a class="abs read" style="left:616px;top:641px">READ MORE ›</a>
  <div class="abs rule" style="left:592px;top:660px;width:208px"></div>

  <h2 class="abs h services-h">Services &amp; Projects</h2>
  <div class="abs card-img" style="left:40px;background:linear-gradient(120deg,#6a4a30,#d8a888 40%,#f4f0ea 75%)" role="img" aria-label="Hand signing a document with a pen"></div>
  <div class="abs card-img" style="left:299px;background:linear-gradient(90deg,#2e3e5c,#9aa4b4 45%,#e8ecf0 55%,#25324d)" role="img" aria-label="Two business people shaking hands"></div>
  <div class="abs card-img" style="left:558px;background:linear-gradient(90deg,var(--photo-grey),#2b2f3c 30%,#1d2230 70%,var(--photo-grey))" role="img" aria-label="Group of business professionals standing together"></div>

  <div class="abs card-text" style="left:45px">
    <div class="t">Cloud Server Storage Features</div>
    <div class="d">Cloud backup solutions are becoming more and more common these days, with plans ...<br>So that the website can achieve top position and ranking in the Internet searches and thereby increasing</div>
  </div>
  <div class="abs card-text" style="left:302px">
    <div class="t">Cloud Server Storage Features</div>
    <div class="d">Cloud backup solutions are becoming more and more common these days, with plans ...<br>So that the website can achieve top position and ranking in the Internet searches and thereby increasing</div>
  </div>
  <div class="abs card-text" style="left:557px">
    <div class="t">Cloud Server Storage Features</div>
    <div class="d">Cloud backup solutions are becoming more and more common these days, with plans ...<br>So that the website can achieve top position and ranking in the Internet searches and thereby increasing</div>
  </div>
  <div class="abs rule" style="left:45px;top:909px;width:230px"></div>
  <div class="abs rule" style="left:302px;top:909px;width:230px"></div>
  <div class="abs rule" style="left:557px;top:909px;width:230px"></div>
  <a class="abs read" style="left:46px;top:915px">READ MORE ›</a>
  <a class="abs read" style="left:302px;top:915px">READ MORE ›</a>
  <a class="abs read" style="left:558px;top:916px">READ MORE ›</a>

  <footer class="abs footer"></footer>
  <h3 class="abs h f-h" style="left:30px">Company</h3>
  <ul class="abs f-list" style="left:30px"><li>Mainpage</li><li>Why We Are</li><li>Why Choose Us</li><li>Testimonials</li><li>Recent Blog</li></ul>
  <div class="abs f-sep" style="left:125px"></div>
  <h3 class="abs h f-h" style="left:148px">About us</h3>
  <ul class="abs f-list" style="left:148px;top:1006px"><li>Our Mission</li><li>Overvices</li><li>Projects Report</li><li>About Us</li></ul>
  <div class="abs f-sep" style="left:248px"></div>
  <h3 class="abs h f-h" style="left:276px">Support &amp; FAQ's</h3>
  <ul class="abs f-list" style="left:275px;top:1008px"><li>FAQ</li><li>Our Support</li><li>Contact Form</li><li>Contact info</li></ul>
  <div class="abs f-sep" style="left:398px"></div>
  <h3 class="abs h f-h" style="left:422px">Get in touch</h3>
  <div class="abs social">
    <div><i></i>Friendsheet</div>
    <div><i></i>Chirper</div>
    <div><i></i>Linkwork</div>
  </div>

  <aside class="abs news"></aside>
  <h3 class="abs h news-h">Newsletter Sign up</h3>
  <div class="abs field" style="top:1010px">your name</div>
  <div class="abs field" style="top:1042px">your email address</div>
  <a class="abs subscribe">Subscribe ›</a>

  <div class="abs copy-rule"></div>
  <div class="abs copyright">© Copyright 2011 Corvane.com - All Rights Reserved</div>
</div>
</body>
</html>
```